Veteran Owned General Contractor needs Bold New Business Cards

We are a service disabled veteran owned small business. We're a general contractor that specializes in excavation, underground utilities, site work, land clearing and demolition. We would like a fresh, simple, bold, new look for our business cards. We're open to ideas! We'd like to incorporate the following information on the card:

Company Name & Logo, Name of Person, Job Title, Office Phone, Fax, Cell Phone, Email Address, Website, SDVOSB

Our logo is included. We look forward to your thoughts.

Thank you!
Updates

Reason: Hello Due to the overwhelming response to this project, we are extending the deadline one time to allow for improved communication and feedback with the top candidates. We would like to thank everyone for their hard work and exceptional creativity! Thank you

Industry/Entity Type

Business

Contact Information for Business Card

Font styles to use
Sans Serif

Requirements
Nice to have
• As we are a veteran owned company, it would be nice to incorporate an American flag into the design. Maybe on the back?

```html
<!DOCTYPE html>
<html lang="en">
<head>
<meta charset="utf-8">
<title>Keystone4 Inc – Business Card</title>
<link href="https://fonts.googleapis.com/css2?family=Roboto:wght@400;500;700&display=swap" rel="stylesheet">
<style>
  :root {
    --page-bg: #e9e9e7;
    --card-bg: #ffffff;
    --brand-green: #6abf45;
    --text-grey: #6d6e70;
    --mark-dark: #3a3b3d;
  }
  * { margin: 0; padding: 0; box-sizing: border-box; }
  html, body {
    width: 1200px; height: 1200px; overflow: hidden;
    background: var(--page-bg);
    font-family: "Roboto", Arial, sans-serif;
  }
  .canvas { position: relative; width: 1200px; height: 1200px; }
  .card {
    position: absolute; left: 214px; width: 771px; height: 440px;
    background: var(--card-bg);
    box-shadow: 0 2px 8px rgba(0,0,0,0.15);
  }
  .card--front { top: 150px; }
  .card--back { top: 633px; }

  .brand { display: flex; align-items: center; gap: 10px; }
  .brand__square {
    width: 50px; height: 50px; border-radius: 6px; background: var(--mark-dark);
  }
  .brand__name {
    font-weight: 700; color: var(--brand-green);
    letter-spacing: 2px; line-height: 1;
  }
  .card--front .brand { position: absolute; left: 51px; top: 54px; }
  .card--front .brand__name { font-size: 44px; }

  .person { position: absolute; left: 51px; top: 132px; }
  .person__name { font-size: 27px; font-weight: 500; color: var(--brand-green); line-height: 1.2; }
  .person__title { font-size: 20px; color: var(--text-grey); margin-top: 2px; }

  .address {
    position: absolute; left: 51px; top: 218px;
    font-size: 19px; line-height: 26px; color: var(--text-grey); font-style: normal;
  }
  .contacts { position: absolute; left: 51px; top: 286px; list-style: none; }
  .contacts__item {
    display: flex; align-items: center; gap: 7px;
    font-size: 19px; line-height: 27.5px; color: var(--text-grey);
  }
  .contacts__icon { width: 18px; height: 18px; flex: none; }

  .card--back .brand {
    position: absolute; left: 0; right: 0; top: 184px; justify-content: center;
  }
  .card--back .brand__square { width: 70px; height: 70px; border-radius: 8px; }
  .card--back .brand__name { font-size: 60px; }
  .back-web {
    position: absolute; left: 0; right: 0; top: 383px; text-align: center;
    font-size: 21px; color: var(--text-grey);
  }
  .back-web__accent { color: var(--brand-green); }
</style>
</head>
<body>
<div class="canvas">
  <section class="card card--front">
    <div class="brand">
      <span class="brand__square"></span>
      <span class="brand__name">KEYSTONE4 INC</span>
    </div>
    <div class="person">
      <div class="person__name">Daniel Harper</div>
      <div class="person__title">President &amp; CEO</div>
    </div>
    <address class="address">
      2750 Alder Road, Suite 310<br>
      Fairview, CA 95012
    </address>
    <ul class="contacts">
      <li class="contacts__item">
        <svg class="contacts__icon" viewBox="0 0 24 24" fill="none" stroke="#6abf45" stroke-width="1.8"><path d="M5 3h4l2 5-2.5 1.5a11 11 0 0 0 6 6L16 13l5 2v4a2 2 0 0 1-2 2A17 17 0 0 1 3 5a2 2 0 0 1 2-2z"/></svg>
        000-000-0000
      </li>
      <li class="contacts__item">
        <svg class="contacts__icon" viewBox="0 0 24 24" fill="none" stroke="#6abf45" stroke-width="1.8"><rect x="6" y="2" width="12" height="20" rx="2"/><line x1="11" y1="18" x2="13" y2="18"/></svg>
        000-000-0000
      </li>
      <li class="contacts__item">
        <svg class="contacts__icon" viewBox="0 0 24 24" fill="none" stroke="#6abf45" stroke-width="1.8"><rect x="2" y="5" width="20" height="14"/><path d="M2 5l10 8 10-8M2 19l7-7M22 19l-7-7"/></svg>
        d.harper@sample-site.com
      </li>
      <li class="contacts__item">
        <svg class="contacts__icon" viewBox="0 0 24 24" fill="none" stroke="#6abf45" stroke-width="1.8"><circle cx="12" cy="12" r="10"/><ellipse cx="12" cy="12" rx="4.5" ry="10"/><line x1="2" y1="12" x2="22" y2="12"/><path d="M4 7h16M4 17h16"/></svg>
        www.sample-site.com
      </li>
    </ul>
  </section>

  <section class="card card--back">
    <div class="brand">
      <span class="brand__square"></span>
      <span class="brand__name">KEYSTONE4 INC</span>
    </div>
    <div class="back-web">www.<span class="back-web__accent">sample-site</span>.com</div>
  </section>
</div>
</body>
</html>
```